Journal Cover Design Project

The Worldwide Review of Rising Trade Systems is a professional journal which aims to provide an international platform for publication of original research on the emerging economies.
The journal is published three times a year and available by subscription. Currently, the cover design is the same for each issue. We are looking to redesign the cover (and interior) of our journal and would like a design that would allow us to change the color scheme for each issue or volume while maintaining a consistent design scheme.
Our design preference is simple and modern with good use of color. Many of our past publications have used abstract maps/globes but we are open to new ideas. We would need a creative way to include text on the cover, possibly a way to present the article titles or main topics for each issue. For example, we like the use of color and the general design in this image: http://www.pixmoravo.example/photos/drawdreamhope/5182640913/lightbox/
Below is a link to our most recent issue of the journal. You can see an example of the article titles, structure, etc. The website also shows the current cover of the journal (but we do not want the new design to be based off of the current one):
http://rts.quilberpress.example/content/4/2.toc

```html
<!DOCTYPE html>
<html lang="en">
<head>
<meta charset="utf-8">
<title>Trade and Transport in Central Asia — Journal Spread</title>
<link rel="stylesheet" href="https://fonts.googleapis.com/css2?family=Playfair+Display:wght@700;900&family=Source+Sans+3:wght@400;600;700&family=Source+Serif+4:wght@400&display=swap">
<style>
  :root {
    --backdrop: #2f3539;
    --page-white: #ffffff;
    --page-tint: #dfe1ea;
    --navy: #0d3a62;
    --navy-deep: #062a4a;
    --mark-blue: #3f6a92;
    --accent-red: #d0202a;
    --ink: #1d1d1f;
    --ink-soft: #333338;
    --rule: #55585f;
  }
  * { margin: 0; padding: 0; box-sizing: border-box; }
  html, body { width: 1200px; height: 900px; overflow: hidden; }
  body {
    background: var(--backdrop);
    position: relative;
    font-family: "Source Sans 3", sans-serif;
    color: var(--ink);
  }
  .spread { position: absolute; left: 25px; top: 42px; width: 1151px; height: 754px; display: flex; }
  .page { position: relative; height: 100%; }
  .page--contents { width: 575px; background: var(--page-white); }
  .page--opener { width: 576px; background: var(--page-tint); }

  /* Contents page */
  .contents-heading {
    position: absolute; left: 94px; top: 70px;
    font-size: 18px; font-weight: 600; letter-spacing: 0.4px;
  }
  .contents-entry { position: absolute; left: 0; width: 100%; }
  .entry-page {
    position: absolute; right: 491px; top: -10px;
    font-family: "Playfair Display", serif; font-weight: 900;
    font-size: 35px; line-height: 1; color: var(--navy);
  }
  .entry-text { position: absolute; left: 94px; top: 0; width: 400px; }
  .entry-title {
    font-size: 11px; font-weight: 700; letter-spacing: 0.5px;
    line-height: 17px; text-transform: uppercase;
  }
  .entry-author { font-size: 12px; line-height: 17px; color: var(--ink-soft); }
  .entry-author span { text-transform: uppercase; }

  /* Opener page */
  .masthead {
    position: absolute; left: 0; top: 0; width: 100%; height: 74px;
    background: linear-gradient(90deg, var(--navy-deep) 0%, var(--navy) 55%, var(--navy-deep) 100%);
  }
  .masthead-name {
    position: absolute; right: 94px; top: 30px;
    font-weight: 700; font-size: 42px; line-height: 44px;
    letter-spacing: 1px; color: var(--mark-blue);
  }
  .masthead-rule { position: absolute; left: 0; top: 78px; width: 100%; height: 5px; background: var(--accent-red); }

  .article-title {
    position: absolute; right: 94px; top: 138px;
    text-align: right; font-family: "Playfair Display", serif;
    font-weight: 900; font-size: 38px; line-height: 46px;
  }
  .article-author {
    position: absolute; right: 94px; top: 249px;
    font-size: 12.5px; font-weight: 600; letter-spacing: 0.5px;
  }
  .abstract-heading {
    position: absolute; left: 47px; top: 346px;
    font-size: 15.5px; font-weight: 700; letter-spacing: 0.5px;
  }
  .abstract-body {
    position: absolute; left: 47px; top: 383px; width: 436px;
    font-size: 12.4px; line-height: 17.2px; text-align: justify;
    color: var(--ink-soft);
  }
  .abstract-body .lead { font-weight: 700; letter-spacing: 0.4px; color: var(--ink); }
  .notes-rule { position: absolute; left: 47px; top: 598px; width: 436px; height: 1px; background: var(--rule); }
  .notes {
    position: absolute; left: 47px; top: 607px; width: 436px;
    font-family: "Source Serif 4", serif; font-size: 8.6px; line-height: 17px;
    text-align: justify; color: var(--ink-soft);
  }
  .notes b { font-family: "Source Sans 3", sans-serif; font-weight: 700; font-size: 9.4px; color: var(--ink); }
  .folio {
    position: absolute; right: 94px; top: 697px;
    font-size: 8.6px; letter-spacing: 0.6px; text-transform: uppercase; color: var(--ink-soft);
    display: flex; align-items: center; gap: 8px;
  }
  .folio-number { font-weight: 700; font-size: 9px; }
</style>
</head>
<body>
  <main class="spread">
    <section class="page page--contents">
      <h2 class="contents-heading">ARTICLES</h2>

      <article class="contents-entry" style="top:128px">
        <div class="entry-page">4</div>
        <div class="entry-text">
          <p class="entry-title">Editorial</p>
          <p class="entry-author">by <span>Aren Solvik</span></p>
        </div>
      </article>

      <article class="contents-entry" style="top:180px">
        <div class="entry-page">7</div>
        <div class="entry-text">
          <p class="entry-title">Trade and Transport in Central Asia</p>
          <p class="entry-author">by <span>Roland Pelverin</span></p>
        </div>
      </article>

      <article class="contents-entry" style="top:231px">
        <div class="entry-page">11</div>
        <div class="entry-text">
          <p class="entry-title">Central Asia’s Oil and Gas Reserves: To Whom Do They Matter?</p>
          <p class="entry-author">by <span>Marta Brenn Oakhurst</span></p>
        </div>
      </article>

      <article class="contents-entry" style="top:283px">
        <div class="entry-page">16</div>
        <div class="entry-text">
          <p class="entry-title">How Bad Are Central Asia’s Business Environments<br>and What Can Be Done About Them?</p>
          <p class="entry-author">by <span>Dorian de Valle</span></p>
        </div>
      </article>

      <article class="contents-entry" style="top:352px">
        <div class="entry-page">21</div>
        <div class="entry-text">
          <p class="entry-title">“Asiaregio”: An Institutional Model to Deepen Integration<br>in Central Asia’s Border Regions</p>
          <p class="entry-author">by <span>Bartosz Kelmarski, Marat Khodirov, Sunaya Mehtar</span><br>and <span style="text-transform:none">Gaëtan Rabelier</span></p>
        </div>
      </article>
    </section>

    <section class="page page--opener">
      <header class="masthead"><div class="masthead-name">WRRTS</div></header>
      <div class="masthead-rule"></div>

      <h1 class="article-title">Trade and Transport<br>in Central Asia</h1>
      <p class="article-author">ROLAND PELVERIN</p>

      <h3 class="abstract-heading">ABSTRACT</h3>
      <p class="abstract-body"><span class="lead">UNTIL 1991, CENTRAL ASIA WAS PART</span> of the integrated economic space of the Soviet Union without borders Maximihil ta mor unum labus, sa re nem re culium ia L. Vivati, crisse pereo, publinteatum meisunt. Caesilis, caperce retiusque ad aurnit. Nihicap ecivid patimpl. Equam que ia? Ucia? quast nem, oca; nonsidees nir ut apero intiam hos vis. Sentimoraris ad firtus eredo, movidem senatus, vidienit, que caes sensus pribut idem hi, quem omnerte riamdiere antror quam. Erid Catebus cavehena, vesusqua qua nonsultus occulleressi conem que consimihin tis conc rediente vas eludac res menihilius; nestiaed in hena, ut cae nor ia tem in ad patum parbis. Equeriuri cerfeco inata at, con in in ium hos culoctes ad scips, que rehendesuam tabunum acie mena, cons in diuro ia peretiae etori simurs pulerio con se, et; C. Opiore omnost C. Sp. Ex noriam, coniquam. Iqui periosse in ta porent, aber ist mors face terdic mandem orioniam.</p>

      <div class="notes-rule"></div>
      <div class="notes">
        <p><b>Acknowledgements.</b> Airtus eredo, movidem sete dolobor et etummy nonullan vel eugait niam ea augait acincidunt do endreet iure minim ipisi blan heniat. Uptat lor iure te dolore tet, vullaor in euga.</p>
        <p><b>Roland Pelverin</b> is Professor of Economics. University of Westmarch, Australia. E-mail:</p>
      </div>

      <footer class="folio">
        <span>Worldwide Review of Rising Trade Systems</span>
        <svg width="8" height="8" viewBox="0 0 8 8" aria-hidden="true"><path d="M4 0 L5 3 L8 4 L5 5 L4 8 L3 5 L0 4 L3 3 Z" fill="var(--ink)"/></svg>
        <span class="folio-number">7</span>
      </footer>
    </section>
  </main>
</body>
</html>
```